menu for prepared meals company

Currently have a menu set up with company logo, would like something more eye catching and artistic to make it look professional. This is a fitness and health driven company in regards to purchasing prepared meals to use towards fitness goals. Do not necessarily want the menu to be geared towards muscular men and women. Looking to have the menu be simple to understand, exactly what it stands for, and geared towards a large demographic in health and life style eating changes.

Target Market(s)

health/fitness

Industry/Entity Type

It Company

Requirements
Must have
• *please see set up for mock menu and apply changes that were applied in the word document menu information.
• ex:do not offer sweet potato and chicken hash*

```html
<!DOCTYPE html>
<html lang="en">
<head>
<meta charset="utf-8">
<title>Fresh Fuel Kitchen Menu</title>
<link rel="stylesheet" href="https://fonts.googleapis.com/css2?family=Kaushan+Script&family=Roboto:wght@400;700;900&family=Roboto+Slab:wght@400;700&display=swap">
<style>
:root{
  --red:#e0231c;
  --ink:#1b1b1b;
  --paper:#ffffff;
  --soft:#e9e9e9;
}
*{margin:0;padding:0;box-sizing:border-box}
html,body{width:729px;height:1200px;overflow:hidden;background:var(--paper)}
body{position:relative;font-family:"Roboto",Arial,sans-serif;color:var(--ink)}
.ribbon{position:absolute;display:flex;align-items:center;justify-content:center}
.ribbon svg{position:absolute;inset:0}
.ribbon-title{position:relative;font-family:"Kaushan Script",cursive;color:#fff;font-size:31px;line-height:1}
.meal-name{position:absolute;left:28px;font-weight:900;color:var(--red);font-size:17px}
.meal-desc{position:absolute;left:28px;font-size:13.5px;font-weight:700;line-height:17px}
.meal-price{position:absolute;right:40px;font-family:"Roboto Slab",serif;font-size:15px}
.dash{position:absolute;left:22px;right:22px;border-top:2px dashed var(--ink)}
.veg-band{position:absolute;left:20px;right:20px;top:384px;height:88px;
  background:linear-gradient(90deg,var(--soft),#f6f6f6 35%,#fff 50%,#f6f6f6 65%,var(--soft))}
.brand{position:absolute;left:0;right:0;top:404px;text-align:center}
.brand-name{display:inline-flex;align-items:center;gap:8px;font-family:"Kaushan Script",cursive;font-size:34px;color:var(--red);background:#fff;padding:0 14px}
.brand-dot{width:12px;height:12px;border-radius:50%;background:var(--red)}
.center{position:absolute;left:0;right:0;text-align:center}
.protein-head{font-weight:900;color:var(--red);font-size:16px}
.protein-sub{font-size:13px;font-weight:700}
.col-head{position:absolute;font-size:11px;font-weight:700;text-align:center;line-height:13px}
.p-name{position:absolute;font-weight:900;color:var(--red);font-size:15px}
.p-price{position:absolute;font-family:"Roboto Slab",serif;font-size:14.5px}
.side-head{position:absolute;font-weight:900;font-size:15px;text-align:center;line-height:17px}
.side-head small{font-size:13px;font-weight:700}
.side-item{position:absolute;font-weight:900;color:var(--red);font-size:15px;text-align:center}
.note{font-weight:900;font-size:15px;line-height:19px}
</style>
</head>
<body>

<div class="ribbon" style="left:12px;top:29px;width:304px;height:50px">
  <svg viewBox="0 0 304 50" preserveAspectRatio="none"><polygon points="0,0 304,0 288,25 304,50 0,50" fill="#1b1b1b"/><line x1="6" y1="6" x2="290" y2="6" stroke="#e0231c" stroke-width="1.5"/><line x1="6" y1="44" x2="290" y2="44" stroke="#e0231c" stroke-width="1.5"/></svg>
  <span class="ribbon-title">Specialty Meals</span>
</div>

<section class="specialty">
  <div class="meal-name" style="top:100px">Pasta with Turkey Meatballs</div>
  <div class="meal-desc" style="top:120px">Whole grain pasta with turkey meatballs and a tomato sauce</div>
  <div class="meal-price" style="top:110px">$ 9.95</div>

  <div class="meal-name" style="top:166px">Stir Fry</div>
  <div class="meal-desc" style="top:186px">Chicken, stir fry vegetable mix with jasmine rice</div>
  <div class="meal-price" style="top:176px">$ 9.95</div>

  <div class="meal-name" style="top:232px">Stuffed Pepper</div>
  <div class="meal-desc" style="top:252px">Pepper stuffed with ground turkey,<br>your choice of whole grain or jasmine rice combined in a red sauce</div>
  <div class="meal-price" style="top:245px">$ 9.95</div>

  <div class="meal-name" style="top:315px">Turkey Burger</div>
  <div class="meal-desc" style="top:335px">Turkey patty on a multigrain flat bread with side of sweet potato fries</div>
  <div class="meal-price" style="top:325px">$ 9.95</div>
</section>

<div class="veg-band" role="img" aria-label="Row of grey line-drawn vegetables and herbs"></div>
<div class="brand"><span class="brand-name"><span class="brand-dot"></span>Fresh Fuel Kitchen</span></div>

<div class="dash" style="top:497px"></div>

<div class="ribbon" style="left:200px;top:512px;width:329px;height:48px">
  <svg viewBox="0 0 329 48" preserveAspectRatio="none"><polygon points="0,0 329,0 314,24 329,48 0,48 15,24" fill="#1b1b1b"/><line x1="18" y1="6" x2="311" y2="6" stroke="#e0231c" stroke-width="1.5"/><line x1="18" y1="42" x2="311" y2="42" stroke="#e0231c" stroke-width="1.5"/></svg>
  <span class="ribbon-title">Create Your Own</span>
</div>

<div class="center protein-head" style="top:564px">Choose Your Protein</div>
<div class="center protein-sub" style="top:585px">pick your protein and serving size</div>

<div class="col-head" style="left:276px;top:612px;width:60px">Half size<br>4oz</div>
<div class="col-head" style="left:380px;top:612px;width:60px">Full size<br>6oz</div>
<div class="col-head" style="left:584px;top:618px;width:40px">6oz</div>

<div class="p-name" style="left:49px;top:642px">Chicken</div>
<div class="p-name" style="left:49px;top:671px">Ground Beef</div>
<div class="p-name" style="left:49px;top:701px">Ground Turkey</div>
<div class="p-name" style="left:49px;top:730px">Turkey Tenderloin</div>
<div class="p-name" style="left:49px;top:759px">Steak</div>

<div class="p-price" style="left:280px;top:642px">$ 7.95</div>
<div class="p-price" style="left:280px;top:671px">$ 7.95</div>
<div class="p-price" style="left:280px;top:701px">$ 7.95</div>
<div class="p-price" style="left:280px;top:730px">$ 7.95</div>
<div class="p-price" style="left:280px;top:759px">$ 9.95</div>
<div class="p-price" style="left:384px;top:642px">$ 8.95</div>
<div class="p-price" style="left:384px;top:671px">$ 8.95</div>
<div class="p-price" style="left:384px;top:701px">$ 8.95</div>
<div class="p-price" style="left:384px;top:730px">$ 8.95</div>
<div class="p-price" style="left:384px;top:759px">$10.95</div>

<div class="p-name" style="left:450px;top:642px">Salmon</div>
<div class="p-name" style="left:450px;top:671px">Tilapia</div>
<div class="p-name" style="left:450px;top:701px">Cod</div>
<div class="p-name" style="left:450px;top:759px">Veggie Burger</div>
<div class="p-price" style="left:578px;top:642px">$ 11.95</div>
<div class="p-price" style="left:578px;top:671px">$ 10.95</div>
<div class="p-price" style="left:578px;top:701px">$ 9.95</div>
<div class="p-price" style="left:578px;top:759px">$ 9.95</div>

<div class="dash" style="top:806px"></div>

<div class="ribbon" style="left:70px;top:833px;width:272px;height:46px">
  <svg viewBox="0 0 272 46" preserveAspectRatio="none"><polygon points="0,0 272,0 258,23 272,46 0,46 14,23" fill="#1b1b1b"/><line x1="16" y1="6" x2="256" y2="6" stroke="#e0231c" stroke-width="1.5"/><line x1="16" y1="40" x2="256" y2="40" stroke="#e0231c" stroke-width="1.5"/></svg>
  <span class="ribbon-title" style="font-size:28px">Vegetable Choices</span>
</div>
<div class="ribbon" style="left:398px;top:833px;width:272px;height:46px">
  <svg viewBox="0 0 272 46" preserveAspectRatio="none"><polygon points="0,0 272,0 258,23 272,46 0,46 14,23" fill="#1b1b1b"/><line x1="16" y1="6" x2="256" y2="6" stroke="#e0231c" stroke-width="1.5"/><line x1="16" y1="40" x2="256" y2="40" stroke="#e0231c" stroke-width="1.5"/></svg>
  <span class="ribbon-title" style="font-size:28px">Carb Choices</span>
</div>

<div class="side-head" style="left:100px;top:886px;width:90px">Half size<br><small>1/2 cup</small></div>
<div class="side-head" style="left:196px;top:886px;width:90px">Full size<br><small>1 cup</small></div>
<div class="side-head" style="left:438px;top:886px;width:90px">Half size<br><small>1/2 cup</small></div>
<div class="side-head" style="left:534px;top:886px;width:90px">Full size<br><small>1 cup</small></div>

<div class="side-item" style="left:86px;width:240px;top:934px">Broccoli</div>
<div class="side-item" style="left:86px;width:240px;top:965px">Asparagus</div>
<div class="side-item" style="left:86px;width:240px;top:995px">Spinach</div>
<div class="side-item" style="left:86px;width:240px;top:1026px">Green Beans</div>
<div class="side-item" style="left:400px;width:280px;top:934px">Whole Grain Pasta/Gluten Free Pasta</div>
<div class="side-item" style="left:400px;width:280px;top:965px">Whole Grain Rice</div>
<div class="side-item" style="left:400px;width:280px;top:995px">Jasmine Rice</div>
<div class="side-item" style="left:400px;width:280px;top:1026px">Sweet Potato</div>

<div class="dash" style="top:1075px"></div>

<div class="center note" style="top:1096px">If you prefer 2 vegetable choices<br>we recommend you to choose 2 to our low carb choices meal combo.</div>
<div class="center note" style="top:1150px">Opens for delivery within 20 miles for small fee.</div>

<div class="dash" style="top:1188px"></div>

</body>
</html>
```